Law Firm Needs Brochure Redesign Using New Logo

We are a personal injury law firm that does auto injuries and other personal injury cases. We want a new brochure that has our updated logo and information. Instead of gold and black, we want more navy, as matches the new logo. The Auto Liability portion should read: "(required by the state of Arizona in the amounts of $25,000 per person / $50,000 per accident, but a higher amount may be best )." The other information can remain the same. We'd like the brochure to keep the same professional tone as the previous brochure.
Our website is https://www.marbrenlegal.com/.

```html
<!DOCTYPE html>
<html lang="en">
<head>
<meta charset="utf-8">
<title>Marbren Legal – Car Accident Brochure</title>
<link href="https://fonts.googleapis.com/css2?family=Poppins:wght@400;500;600;700;800&family=Oswald:wght@400;500&display=swap" rel="stylesheet">
<style>
:root{
  --navy:#13274a;
  --navy-deep:#0d1d38;
  --navy-mid:#2c4670;
  --slate:#c6cfda;
  --slate-text:#c9d3e0;
  --ink:#13274a;
  --white:#ffffff;
  --page:#e4e5e7;
}
*{box-sizing:border-box;margin:0;padding:0}
html,body{width:1200px;height:2666px;overflow:hidden;background:var(--page);font-family:"Poppins",sans-serif;color:var(--white)}
.spread{position:absolute;left:60px;width:1080px;height:838px;display:flex;box-shadow:0 6px 18px rgba(0,0,0,.25)}
.spread--outside{top:330px}
.spread--inside{top:1498px}
.panel{position:relative;width:360px;height:100%;overflow:hidden;background:var(--navy)}
.photo{position:absolute;left:0;width:100%}
.band{position:absolute;left:0;width:100%;height:100%;top:0}

/* outside left */
.photo--mountain-car{top:0;height:400px;background:linear-gradient(180deg,#f1f2f3 0%,#9a9b9e 30%,#6d6f73 45%,#cfd0d2 62%,#e9eaeb 100%);clip-path:polygon(0 0,100% 0,100% 100%,0 86%)}
.stats{position:absolute;left:22px;right:22px;top:410px;height:144px;border:1.5px solid rgba(255,255,255,.75);border-radius:8px;display:flex}
.stat{flex:1;padding:14px 16px}
.stat+.stat{border-left:1.5px dashed rgba(255,255,255,.6);flex:.75}
.stat__over{font-size:14px;font-weight:600;letter-spacing:.5px}
.stat__num{font-family:"Oswald",sans-serif;font-size:41px;font-weight:400;line-height:1.1}
.stat__text{font-size:12.5px;line-height:1.2;font-weight:500}
.promise{position:absolute;left:34px;right:34px;top:596px;height:158px;background:var(--slate);border-radius:4px;color:var(--ink);font-size:12.6px;font-weight:600;line-height:1.18;text-align:center;padding:24px 18px}
.site{position:absolute;left:0;right:0;top:785px;text-align:center;font-size:14.5px;letter-spacing:2.4px;font-weight:500}

/* outside middle */
.panel--flap{background:var(--white)}
.flap-id{position:absolute;left:22px;bottom:30px;writing-mode:vertical-rl;transform:rotate(180deg);display:flex;gap:10px;color:var(--ink)}
.flap-id__name{font-size:19px;font-weight:800;letter-spacing:1px}
.flap-id__addr{font-size:12px;font-weight:600;line-height:1.25}

/* outside right: cover */
.cover-top{position:absolute;top:0;left:0;width:100%;height:130px;background:linear-gradient(180deg,#dfe3e8,#c4c9cf)}
.brand{position:absolute;top:42px;left:0;right:0;display:flex;align-items:center;justify-content:center;gap:10px;color:var(--ink);font-weight:800;font-size:27px;letter-spacing:1px}
.brand__dot{width:22px;height:22px;border-radius:50%;background:var(--ink)}
.photo--suv{top:110px;height:430px;background:linear-gradient(180deg,#9ea3a9 0%,#7f8fa6 35%,#a9b6c7 60%,#5d6672 100%);clip-path:polygon(0 0,100% 0,100% 74%,0 100%)}
.headline{position:absolute;left:24px;right:18px;top:580px;color:var(--slate-text);font-weight:800;font-size:31.5px;line-height:1.1;letter-spacing:.5px;text-transform:uppercase}
.headline span{display:block}
.headline .light{font-weight:600;font-size:27px}
.dots{position:absolute;top:708px;left:0;right:0;display:flex;justify-content:center;gap:3px}
.dots i{width:5px;height:5px;background:var(--slate-text);display:block}
.tagline{position:absolute;top:728px;left:0;right:0;text-align:center;font-size:15px;line-height:1.2}
.site-btn{position:absolute;top:782px;left:50%;transform:translateX(-50%);background:var(--slate);color:var(--ink);border:1.5px solid #fff;border-radius:5px;font-size:14.5px;font-weight:500;padding:1px 10px;white-space:nowrap;letter-spacing:.5px}

/* inside */
.section-title{font-size:17.5px;font-weight:600;text-transform:uppercase;letter-spacing:.2px}
.tips-panel{padding:28px 22px 0 22px}
.tips{list-style:none;margin-top:10px}
.tip{display:flex;align-items:center;gap:20px;height:77.5px;border-bottom:1px solid rgba(255,255,255,.25);font-size:11.6px;line-height:1.18}
.tip:last-child{border-bottom:none}
.tip__num{flex:0 0 46px;height:46px;border-radius:50%;background:var(--white);border:4px solid #9fb0c6;color:var(--ink);font-family:"Oswald",sans-serif;font-size:23px;display:flex;align-items:center;justify-content:center}
.tip b{font-weight:700}
.coverage-panel{padding:28px 20px 0 20px;background:linear-gradient(180deg,var(--navy) 60%,var(--navy-mid) 100%)}
.coverage-intro{font-size:12.4px;line-height:1.15;margin-top:6px}
.photo--shield{position:relative;margin-top:20px;height:140px;border-radius:6px;background:linear-gradient(90deg,#0f1a2d 0%,#3c5476 55%,#8aa1bd 100%)}
.plans{margin-top:18px;padding:0 13px}
.plan{background:var(--slate);color:var(--ink);font-size:11.8px;line-height:1.18;height:84px;padding:12px 16px;margin-bottom:14px;border-radius:2px}
.plan b{font-weight:700}
.safety-panel{background:var(--navy)}
.photo--driver{top:0;height:300px;background:linear-gradient(160deg,#2d2e31 0%,#6b6a69 40%,#b9b4ad 70%,#4e5156 100%);clip-path:polygon(0 0,100% 0,100% 55%,0 100%)}
.stripe{position:absolute;top:0;left:0}
.safety{position:absolute;top:306px;left:21px;right:16px}
.safety h3{font-size:17.5px;font-weight:600;text-transform:uppercase;margin-top:8px}
.safety h3+h3,.safety p+h3{margin-top:30px}
.safety p{font-size:12.2px;line-height:1.18;margin-top:14px}
.safety p+p{margin-top:6px}
.safety b{font-weight:700}
.contact{position:absolute;top:544px;left:0;right:0;text-align:center}
.contact__title{display:inline-block;background:var(--slate);color:var(--ink);font-weight:700;font-size:18px;padding:0 10px;border-radius:6px;border:1.5px solid #fff;line-height:1.4}
.contact__item{margin-top:12px;font-size:12.2px;line-height:1.2}
.icon{display:block;margin:0 auto 2px;width:17px;height:17px}
</style>
</head>
<body>

<!-- Outside spread -->
<section class="spread spread--outside">
  <div class="panel panel--stats">
    <div class="photo photo--mountain-car" role="img" aria-label="Photo of a white SUV in front of a dark mountain"></div>
    <svg class="band" viewBox="0 0 360 838" aria-hidden="true"><polygon points="0,346 360,400 360,420 0,370" fill="#2c4670"/></svg>
    <div class="stats">
      <div class="stat"><p class="stat__over">OVER</p><p class="stat__num">107,000</p><p class="stat__text">crashes will happen<br>in the state of<br>Arizona this year</p></div>
      <div class="stat"><p class="stat__over">OVER</p><p class="stat__num">700</p><p class="stat__text">of them<br>will result<br>in fatalities</p></div>
    </div>
    <p class="promise">If we don't win, you don't pay attorney fees. That seems fair to us. Know what's happening with your case, get the answers to your questions and work on getting better with the confidence that you've got an excellent group of people working for you</p>
    <p class="site">www.marbrenlegal.com</p>
  </div>

  <div class="panel panel--flap">
    <div class="flap-id">
      <p class="flap-id__name">MARBREN LEGAL</p>
      <p class="flap-id__addr">4810 N 16th Street Suite B110<br>Phoenix AZ 85016</p>
    </div>
  </div>

  <div class="panel panel--cover">
    <div class="cover-top"></div>
    <div class="brand"><span class="brand__dot"></span>MARBREN LEGAL</div>
    <div class="photo photo--suv" role="img" aria-label="Photo of a silver SUV on an open highway"></div>
    <svg class="band" viewBox="0 0 360 838" aria-hidden="true"><polygon points="0,540 360,428 360,440 0,556" fill="#c6cfda"/></svg>
    <h1 class="headline"><span>Protect your</span><span class="light">family in case of a</span><span>car accident</span></h1>
    <div class="dots"><i></i><i></i><i></i><i></i><i></i><i></i></div>
    <p class="tagline">A little knowledge and preparation<br>go a long way</p>
    <p class="site-btn">www.marbrenlegal.com</p>
  </div>
</section>

<!-- Inside spread -->
<section class="spread spread--inside">
  <div class="panel tips-panel">
    <h2 class="section-title">Top 10 tips to avoid a crash</h2>
    <ol class="tips">
      <li class="tip"><span class="tip__num">1</span><p><b>Anyone making a left turn must wait for all oncoming traffic to clear before proceeding.</b> Yes, even if the light has turned yellow. Wait to be sure that all traffic has stopped.</p></li>
      <li class="tip"><span class="tip__num">2</span><p><b>When your light turns green,</b> check to be sure that no vehicles are entering the intersection late</p></li>
      <li class="tip"><span class="tip__num">3</span><p><b>Allow plenty of room between you and the car in front of you.</b> Traffic can stop in an instant, even if you can't see anything ahead.</p></li>
      <li class="tip"><span class="tip__num">4</span><p><b>Avoid being distracted.</b> Teenagers are especially susceptible to losing focus if there are too many friends in the car.</p></li>
      <li class="tip"><span class="tip__num">5</span><p><b>Keep the volume of your radio down and never wear headphones.</b> Cars are very soundproof these days, but you need to be able to h ear an ambulance or police siren.</p></li>
      <li class="tip"><span class="tip__num">6</span><p><b>Be especially careful on the weekends and early morning hours.</b></p></li>
      <li class="tip"><span class="tip__num">7</span><p><b>Don't speed.</b> Speed is a factor in most crashes. Street lights are timed and the freeway has traffic. It's likely you won't get there much faster even if you do speed</p></li>
      <li class="tip"><span class="tip__num">8</span><p><b>Don't drink</b> and drive. Many cab companies offer a free service to get you home safe.</p></li>
      <li class="tip"><span class="tip__num">9</span><p><b>Use your turn signals.</b> This gives an early warning to vehicles you may not be able to see</p></li>
    </ol>
  </div>

  <div class="panel coverage-panel">
    <h2 class="section-title">Have the right coverage</h2>
    <p class="coverage-intro">Many people don't know about the different kinds of insurance available. In addition to health insurance, we suggest:</p>
    <div class="photo--shield" role="img" aria-label="Photo of a hand touching a car insurance shield symbol"></div>
    <div class="plans">
      <p class="plan"><b>Auto Liability</b> (required by the state of Arizona in the amounts of $25,000 per person / $50,000 per accident, but a higher amount may be best )</p>
      <p class="plan"><b>Uninsured or Underinsured Motorist Coverage.</b> This protects YOU when the other driver doesn't have insurance or not enough</p>
      <p class="plan"><b>Medical Payments Coverage.</b> Up to $5,000 in coverage will be paid out to you no matter who is at fault in an accident and does not need to be reimbursed</p>
      <p class="plan"><b>Medical Payments Coverage.</b> Up to $5,000 in coverage will be paid out to you no matter who is at fault in an accident and does not need to be reimbursed</p>
      <p class="plan"><b>Homeowners / Renters Insurance.</b> Protectsyou in case of injuries on your property as well as damage to your home from covered events</p>
    </div>
  </div>

  <div class="panel safety-panel">
    <svg class="band" viewBox="0 0 360 838" aria-hidden="true"><polygon points="360,560 360,838 120,838" fill="#2c4670"/></svg>
    <div class="photo photo--driver" role="img" aria-label="Photo of hands on a car steering wheel"></div>
    <svg class="stripe" width="360" height="300" viewBox="0 0 360 300" aria-hidden="true"><polygon points="120,300 360,165 360,178 160,300" fill="#ffffff"/></svg>
    <div class="safety">
      <h3>Model safe behavior</h3>
      <p><b>Always buckle up.</b> Always put your children in car seats/boosters that are rated for their height and weight.</p>
      <h3>Never text while driving</h3>
      <p>Studies have shown that texting while driving is as dangerous as driving intoxicated</p>
      <p><b>Show your children that no text is more important than your safety. It can wait.</b></p>
    </div>
    <div class="contact">
      <p class="contact__title">CONTACT US</p>
      <p class="contact__item"><svg class="icon" viewBox="0 0 20 20" aria-hidden="true"><circle cx="10" cy="10" r="9" fill="#fff"/><path d="M7 5.5l2 2-1 1.3c.7 1.4 1.8 2.5 3.2 3.2l1.3-1 2 2-1.2 1.5C9.8 14 6 10.2 5.5 6.7z" fill="#13274a"/></svg>602.555.0147</p>
      <p class="contact__item"><svg class="icon" viewBox="0 0 20 20" aria-hidden="true"><circle cx="10" cy="10" r="9" fill="#fff"/><rect x="5" y="6.5" width="10" height="7" rx="1" fill="#13274a"/><path d="M5.5 7l4.5 3.5L14.5 7" stroke="#fff" stroke-width="1" fill="none"/></svg>info@marbrenlegal.com</p>
      <p class="contact__item"><svg class="icon" viewBox="0 0 20 20" aria-hidden="true"><circle cx="10" cy="10" r="9" fill="#fff"/><circle cx="10" cy="10" r="5" fill="none" stroke="#13274a" stroke-width="1.3"/><path d="M5 10h10M10 5c-2 3-2 7 0 10M10 5c2 3 2 7 0 10" stroke="#13274a" stroke-width="1" fill="none"/></svg>marbrenlegal.com</p>
      <p class="contact__item"><svg class="icon" viewBox="0 0 20 20" aria-hidden="true"><circle cx="10" cy="10" r="9" fill="#fff"/><path d="M10 4.5a3.5 3.5 0 0 0-3.5 3.5c0 2.6 3.5 7 3.5 7s3.5-4.4 3.5-7A3.5 3.5 0 0 0 10 4.5z" fill="#13274a"/><circle cx="10" cy="8" r="1.3" fill="#fff"/></svg>4810 N. 16th Street Suite B110<br>Phoenix AZ 85016</p>
    </div>
  </div>
</section>

</body>
</html>
```